Indy Film Production Company/Studio

We need a business card designed from an existing logo. We are a digital studio/production company that caters to creating genre entertainment, like Action, Horror, and martial arts. The card along with the logo will be used to Brand the company from letter heads to banners. The design will also be used for postcards and Brochures. It should be professional and masculine.
Updates

Thank you to all the designers who have participated. I'm narrowing down who it will be. Thank you again.

Target Market(s)

Investors, Networks, Producers, and actors

Industry/Entity Type

Film Production

Contact Information for Business Card

Benedict Harlowe
Producer/Writer/Director
www.pelvarmotionworks.com

Requirements
Must have
• Website address, Facebook icon and Twitter icon possibly in the back of the card.
Nice to have
• Logline of Company: Follow The Action.

```html
<!DOCTYPE html>
<html lang="en">
<head>
<meta charset="utf-8">
<title>Pelvar Motion Works – Business Card</title>
<link href="https://fonts.googleapis.com/css2?family=Montserrat:wght@400;500;700;800&display=swap" rel="stylesheet">
<style>
  :root {
    --backdrop: #2b2b2b;
    --card: #050505;
    --red: #e8212b;
    --white: #ffffff;
    --grey: #d9d9d9;
  }
  * { margin: 0; padding: 0; box-sizing: border-box; }
  html, body { width: 1200px; height: 900px; overflow: hidden; }
  body {
    background: var(--backdrop);
    font-family: "Montserrat", Arial, sans-serif;
    position: relative;
  }
  .card {
    position: absolute;
    width: 560px;
    height: 320px;
    background: var(--card);
    overflow: hidden;
    box-shadow: 0 10px 30px rgba(0,0,0,.55);
  }
  .card--front { left: 80px; top: 100px; }
  .card--back { left: 560px; top: 480px; }

  .band { position: absolute; left: 0; bottom: 0; width: 560px; height: 40px; }

  .wordmark {
    position: absolute;
    font-weight: 800;
    text-transform: uppercase;
    letter-spacing: 1px;
    line-height: 1.05;
    display: flex;
    align-items: center;
    gap: 14px;
    font-size: 30px;
  }
  .wordmark__square { width: 22px; height: 22px; flex: none; }
  .card--front .wordmark { left: 150px; top: 96px; color: var(--white); }
  .card--front .wordmark__square { background: var(--white); }
  .card--back .wordmark { left: 40px; top: 180px; color: var(--red); }
  .card--back .wordmark__square { background: var(--red); }

  .web-front {
    position: absolute;
    left: 30px;
    bottom: 54px;
    font-size: 17px;
    font-weight: 500;
    color: var(--white);
    letter-spacing: .3px;
  }
  .web-front .accent { color: var(--red); }

  .contact {
    position: absolute;
    right: 26px;
    top: 22px;
    text-align: right;
  }
  .contact__name {
    font-size: 17px;
    font-weight: 500;
    color: var(--red);
    letter-spacing: 1.5px;
    text-transform: uppercase;
  }
  .contact__title {
    font-size: 11px;
    color: var(--grey);
    letter-spacing: 1.2px;
    text-transform: uppercase;
    margin-top: 3px;
  }
  .contact__list { list-style: none; margin-top: 10px; }
  .contact__item {
    font-size: 12px;
    color: var(--grey);
    line-height: 1.45;
    display: flex;
    justify-content: flex-end;
    align-items: center;
    gap: 8px;
  }
  .contact__icon { width: 10px; height: 10px; flex: none; }
  .contact__dot {
    width: 10px; height: 10px; flex: none;
    border-radius: 50%;
    background: var(--red);
  }
  .rule {
    position: absolute;
    left: 30px;
    top: 62px;
    width: 250px;
    height: 2px;
    background: var(--red);
  }
</style>
</head>
<body>

  <section class="card card--front" aria-label="Card front">
    <div class="wordmark">
      <span class="wordmark__square"></span>
      <span>Pelvar<br>Motion Works</span>
    </div>
    <p class="web-front"><span class="accent">www.</span>pelvarmotionworks<span class="accent">.com</span></p>
    <svg class="band" viewBox="0 0 560 40" aria-hidden="true">
      <rect x="0" y="26" width="280" height="14" fill="var(--red)"/>
      <rect x="280" y="14" width="100" height="26" fill="var(--white)"/>
      <rect x="380" y="0" width="180" height="40" fill="var(--red)"/>
    </svg>
  </section>

  <section class="card card--back" aria-label="Card back">
    <div class="rule"></div>
    <div class="contact">
      <p class="contact__name">Benedict Harlowe</p>
      <p class="contact__title">Producer/Writer/Director</p>
      <ul class="contact__list">
        <li class="contact__item">+330 2718-4406
          <svg class="contact__icon" viewBox="0 0 10 10" aria-hidden="true"><path d="M2 0.5 L4 2.8 L3 4 Q4.5 6 6 7 L7.2 6 L9.5 8 L8 9.5 Q3 9 0.5 2 Z" fill="var(--red)"/></svg>
        </li>
        <li class="contact__item">info@pelvarmotionworks.com
          <svg class="contact__icon" viewBox="0 0 10 10" aria-hidden="true"><rect x="0.5" y="2" width="9" height="6.5" fill="none" stroke="var(--red)"/><path d="M0.5 2 L5 6 L9.5 2" fill="none" stroke="var(--red)"/></svg>
        </li>
        <li class="contact__item">www.pelvarmotionworks.com
          <svg class="contact__icon" viewBox="0 0 10 10" aria-hidden="true"><circle cx="5" cy="5" r="4.3" fill="none" stroke="var(--red)"/><path d="M0.7 5 H9.3 M5 0.7 Q2.5 5 5 9.3 M5 0.7 Q7.5 5 5 9.3" fill="none" stroke="var(--red)" stroke-width=".8"/></svg>
        </li>
        <li class="contact__item">/pelvarmotionworks
          <span class="contact__dot" role="img" aria-label="Social profile"></span>
        </li>
        <li class="contact__item">@pelvarmotion
          <span class="contact__dot" role="img" aria-label="Social profile"></span>
        </li>
      </ul>
    </div>
    <div class="wordmark">
      <span class="wordmark__square"></span>
      <span>Pelvar<br>Motion Works</span>
    </div>
    <svg class="band" viewBox="0 0 560 40" aria-hidden="true">
      <rect x="0" y="26" width="280" height="14" fill="var(--red)"/>
      <rect x="280" y="14" width="100" height="26" fill="var(--white)"/>
      <rect x="380" y="0" width="180" height="40" fill="var(--red)"/>
    </svg>
  </section>

</body>
</html>
```